brindlecove.com website design (promote tax and financial services)

I need web design layouts for a 4-6 page website for a finance and tax services business.

Assumptions:
-Responsive design for desktop, laptop, tablet and mobile
-website will not be programmed with any flash elements
-Animation is welcomed
-stock photography may be required (royalty free preferred)
-Prefer to stay away from designs with large images that result in long loading times
-Web design will be pulled through to other digital and print promotional materials that the company develops

The audience is primarily male. Attached is the site and content map, including the company logo

Target Market(s)

individuals and small-to-medium business owners
Primary geographic market = NYC metropolitan area
Secondary geographic market = East Coast USA
Tertiary geographic market = National USA

Any stock photography should represent a diverse population

Industry/Entity Type

Financial Service

Number of Pages Required

5+ page

Font styles to use
Sans Serif

Colors
0758a4
9bcb3b

Requirements
Must have
• -Responsive design that translates nicely to mobile and tablet devices
• -Simple, clean but yet sophisticated design
• -Be in alignment with or a derivative of the logo design (provided with PPT attachment)
• -Compatibility with website programming and coding software
• -Include a countdown to the tax deadline (April 18, 2016)
• -Web-friendly fonts
• -Search box
• -Link to social media properties (via social icons)
• -Include company phone number and clickable link to activate ability to contact company by email
Nice to have
• -Simple animation, as long as it does not impact load time
• -Engaging call-to-action buttons
• -Rotating homepage banners
• -Original icons
• -"About Us" page should have a friendlier, welcoming design
• -Image/Photo caption examples
• -Assume that copy (text) can be minimized to accommodate more visual displays
• -"Continue reading" or "read more" links to expand truncated copy are welcomed
• -A pricing table (not a priority, but nice to have)
Should not have
• Overcrowded design (don't be afraid of white space, if needed)
• too many bells and whistles (flash animation, moving cursors etc.)

```html
<!DOCTYPE html>
<html lang="en">
<head>
<meta charset="utf-8">
<title>Brindle Cove – Tax &amp; Financial Services</title>
<link href="https://fonts.googleapis.com/css2?family=Open+Sans:wght@400;600;700&family=Raleway:wght@400;500;600;700&display=swap" rel="stylesheet">
<style>
:root{
  --blue:#0758a4;
  --blue-deep:#054a8c;
  --blue-bright:#0f6fd0;
  --green:#9bcb3b;
  --green-deep:#6ea51d;
  --ink:#333;
  --muted:#666;
  --line:#e2e2e2;
  --pale:#f2f2f2;
  --dark:#1b1b1b;
  --darker:#111;
}
*{box-sizing:border-box;margin:0;padding:0}
html,body{width:1200px;height:3191px;overflow:hidden}
body{font-family:"Open Sans",Arial,sans-serif;color:var(--ink);background:#fff;font-size:13px;position:relative}
h1,h2,h3,h4{font-family:"Raleway","Open Sans",sans-serif;font-weight:500}

/* top bar */
.topbar{position:absolute;top:0;left:0;width:1200px;height:38px;background:#f4f4f4;border-bottom:1px solid var(--line)}
.social-mini{position:absolute;left:186px;top:10px;display:flex;gap:4px}
.social-mini span{width:16px;height:16px;background:#9a9a9a;border-radius:2px}
.search{position:absolute;left:628px;top:8px;width:218px;height:22px;border:1px solid #ccc;background:#fff;font-size:10px;color:#999;padding:4px 8px}
.search svg{position:absolute;right:6px;top:4px}
.top-mail{position:absolute;left:876px;top:11px;font-size:11px;color:#777;display:flex;align-items:center;gap:6px}

/* header */
.header{position:absolute;top:38px;left:0;width:1200px;height:96px;background:#fff}
.brand{position:absolute;left:186px;top:32px;display:flex;align-items:center;gap:10px;font-family:"Raleway",sans-serif;font-weight:700;font-size:24px;color:var(--blue)}
.brand i{width:22px;height:22px;background:var(--green);display:block}
.nav{position:absolute;left:466px;top:0;display:flex;height:96px}
.nav a{font-family:"Raleway",sans-serif;font-size:14px;color:#555;text-decoration:none;padding:0 14px;line-height:96px;position:relative}
.nav a.active{color:var(--green-deep)}
.nav a.active:after{content:"";position:absolute;left:14px;right:14px;bottom:0;height:4px;background:var(--green)}
.phone{position:absolute;left:890px;top:36px;display:flex;align-items:center;gap:8px;font-size:16px;color:#333;font-weight:600}
.phone b{width:24px;height:24px;border-radius:50%;background:var(--blue);display:flex;align-items:center;justify-content:center}

/* hero */
.hero{position:absolute;top:134px;left:0;width:1200px;height:468px;background:linear-gradient(135deg,#8d8680 0%,#5d5650 40%,#3f3833 75%,#2a2420 100%);color:#fff;text-align:center}
.hero .photo{position:absolute;inset:0}
.hero .shade{position:absolute;inset:0;background:rgba(0,0,0,.25)}
.hero-title{position:absolute;top:106px;left:0;width:1200px;font-family:"Open Sans",sans-serif;font-weight:700;font-size:38px;letter-spacing:.5px;line-height:1}
.hero-sub{position:absolute;top:150px;left:0;width:1200px;font-weight:700;font-size:27px}
.hero-copy{position:absolute;top:192px;left:0;width:1200px;font-size:15px;line-height:1.4}
.hero-cta{position:absolute;top:252px;left:375px;width:212px;height:40px;background:var(--green);color:#fff;font-weight:600;font-size:15px;line-height:40px;border-radius:2px}
.hero-mail{position:absolute;top:262px;left:610px;display:flex;gap:10px;align-items:center;font-size:15px}
.hero-q{position:absolute;top:316px;left:0;width:1200px;font-weight:700;font-size:17px}
.count{position:absolute;top:352px;left:420px;display:flex;gap:8px}
.count div{width:88px;height:90px;border:2px solid #fff;background:rgba(0,0,0,.35);padding-top:6px}
.count strong{display:block;font-size:40px;font-weight:400;line-height:48px}
.count span{font-size:12px;letter-spacing:1px}
.arrow{position:absolute;top:212px}

/* features */
.features{position:absolute;top:602px;left:0;width:1200px;height:282px}
.features svg.band{position:absolute;inset:0}
.feature{position:absolute;top:36px;width:280px;text-align:center;color:#fff}
.feature h3{font-family:"Open Sans",sans-serif;font-weight:400;font-size:18px;margin-top:18px}
.feature p{font-size:10.5px;line-height:1.5;margin-top:6px;color:#dce8f6}
.feature .more{display:inline-block;margin-top:12px;border:1.5px solid #fff;padding:4px 16px;font-size:10px}
.divider{position:absolute;top:20px;width:1px;height:206px;background:rgba(255,255,255,.25)}

/* text blocks */
.block{position:absolute;left:0;width:1200px}
.block h2{font-size:28px;color:#333;font-weight:500}
.block p{font-size:11.5px;line-height:1.65;color:var(--muted);margin-top:12px}
.ph{position:absolute}
.chev{position:absolute;left:578px;width:44px;height:44px;border-radius:50%;background:#fff;border:1px solid #ddd;display:flex;align-items:center;justify-content:center;z-index:3}

/* referral */
.referral{position:absolute;top:1826px;left:0;width:1200px;height:408px;background:linear-gradient(120deg,#3b3b3b,#5a5956 45%,#2a2a2a);color:#fff;text-align:center}
.referral .shade{position:absolute;inset:0;background:rgba(0,0,0,.35)}
.referral h2{position:absolute;top:40px;width:1200px;font-size:33px;font-weight:400}
.referral h3{position:absolute;top:82px;width:1200px;font-size:24px;font-weight:400}
.referral .lead{position:absolute;top:122px;width:1200px;font-size:15px}
.card{position:absolute;top:168px;width:252px;height:192px}
.card .top{height:150px;display:flex;align-items:center;justify-content:center;position:relative}
.card .hex{position:absolute;left:76px;top:12px}
.card .save{position:relative;font-family:"Raleway",sans-serif}
.card .save small{display:block;font-size:18px}
.card .save b{font-size:34px;font-weight:500;line-height:1}
.card .label{height:42px;line-height:42px;font-size:15px;letter-spacing:.5px}

/* faq */
.faq{position:absolute;top:2234px;left:0;width:1200px;height:432px;background:#fff}
.faq h2{position:absolute;top:38px;width:1200px;text-align:center;font-size:27px;font-family:"Open Sans",sans-serif;font-weight:400;color:#222}
.acc{position:absolute;top:98px;left:200px;width:746px;border:1px solid var(--line)}
.acc .row{height:45px;border-top:1px solid var(--line);display:flex;align-items:center;padding:0 16px;font-size:12px;color:#555;position:relative}
.acc .row:first-child{border-top:0}
.acc .row.open{background:var(--blue);color:#fff}
.acc .row b{margin-right:8px;font-weight:600}
.acc .row .tog{position:absolute;right:14px;top:14px;width:18px;height:18px;border-radius:50%;background:#777;display:flex;align-items:center;justify-content:center}
.acc .row.open .tog{background:#fff}
.acc .answer{padding:16px 16px 18px 40px;font-size:11.5px;line-height:1.7;color:#666;position:relative;border-top:1px solid var(--line)}
.acc .answer b{position:absolute;left:16px;top:16px;color:#888}

/* signup */
.signup{position:absolute;top:2666px;left:0;width:1200px;height:240px;background:linear-gradient(135deg,#7cb324,#5f9a14 60%,#4e8a0d)}
.signup h2{position:absolute;top:42px;width:1200px;text-align:center;color:#fff;font-size:28px;font-family:"Open Sans",sans-serif;font-weight:400}
.field{position:absolute;height:34px;background:#fff;font-size:11px;color:#777;padding:10px 10px}
.register{position:absolute;left:728px;top:136px;width:230px;height:34px;background:#1f5a10;color:#fff;font-size:13px;text-align:center;line-height:34px;letter-spacing:.5px}

/* footer */
.footer{position:absolute;top:2906px;left:0;width:1200px;height:222px;background:var(--dark);color:#bbb}
.fcol{position:absolute;top:46px}
.fcol h4{font-family:"Open Sans",sans-serif;font-size:14px;color:#fff;font-weight:400;letter-spacing:.3px;margin-bottom:12px}
.fcol li{list-style:none;font-size:10.5px;line-height:22px;color:#ccc}
.news-in{width:180px;height:24px;background:#fff;color:#999;font-size:9.5px;padding:5px 8px;margin-top:10px}
.sub-btn{display:inline-block;margin-top:12px;background:var(--green);color:#fff;font-size:9.5px;padding:5px 12px}
.contact li{display:flex;align-items:center;gap:6px}
.socials{display:flex;gap:6px;margin-top:10px}
.socials span{width:26px;height:26px;border:1.5px solid #ccc;border-radius:50%}
.foot-brand{position:absolute;left:880px;top:70px;font-family:"Raleway",sans-serif;font-weight:700;font-size:20px;color:#999;display:flex;align-items:center;gap:8px}
.foot-brand i{width:18px;height:18px;background:#777;display:block}
.bottombar{position:absolute;top:3128px;left:0;width:1200px;height:63px;background:var(--darker);color:#999;font-size:10.5px}
.bottombar p{position:absolute;left:187px;top:25px}
</style>
</head>
<body>

<div class="topbar">
  <div class="social-mini"><span></span><span></span><span></span><span></span></div>
  <div class="search">Search here
    <svg width="12" height="12" viewBox="0 0 12 12"><circle cx="5" cy="5" r="3.8" fill="none" stroke="#888" stroke-width="1.4"/><path d="M8 8l3 3" stroke="#888" stroke-width="1.4"/></svg>
  </div>
  <div class="top-mail">
    <svg width="14" height="10" viewBox="0 0 14 10"><rect width="14" height="10" rx="1" fill="#888"/><path d="M0 1l7 5 7-5" stroke="#fff" fill="none"/></svg>
    info@brindlecove.com
  </div>
</div>

<header class="header">
  <div class="brand"><i></i>brindlecove.com</div>
  <nav class="nav">
    <a class="active">HOME</a><a>SERVICES</a><a>ABOUT US</a><a>RESOURCES</a>
  </nav>
  <div class="phone"><b><svg width="12" height="12" viewBox="0 0 12 12"><path d="M3 1l2 2-1 1.5a7 7 0 003.5 3.5L9 7l2 2-1.5 2C5 11 1 7 1 2.5z" fill="#fff"/></svg></b>555.014.2290</div>
</header>

<section class="hero">
  <div class="photo" role="img" aria-label="Desk with calculator, tax forms and a pen"></div>
  <div class="shade"></div>
  <h1 class="hero-title">THE DEADLINE FOR FILING YOUR 2015</h1>
  <div class="hero-sub">FEDERAL TAX RETURN IS APRIL 18, 2016</div>
  <p class="hero-copy">Don't wait! Set up an appointment to file your taxes now and receive<br>the most money from your tax returns</p>
  <div class="hero-cta">Schedule Appointment</div>
  <div class="hero-mail"><svg width="22" height="16" viewBox="0 0 22 16"><rect width="22" height="16" rx="2" fill="#fff"/><path d="M1 2l10 7 10-7" stroke="#555" stroke-width="1.5" fill="none"/></svg>hello@brindlecove.com</div>
  <div class="hero-q">Why is Tax Day April 18?</div>
  <div class="count">
    <div><strong>89</strong><span>DAYS</span></div>
    <div><strong>01</strong><span>HOURS</span></div>
    <div><strong>25</strong><span>MINS</span></div>
    <div><strong>35</strong><span>SEC</span></div>
  </div>
  <svg class="arrow" style="left:156px" width="16" height="28" viewBox="0 0 16 28"><path d="M14 2L3 14l11 12" stroke="#fff" stroke-width="3" fill="none"/></svg>
  <svg class="arrow" style="left:1028px" width="16" height="28" viewBox="0 0 16 28"><path d="M2 2l11 12L2 26" stroke="#fff" stroke-width="3" fill="none"/></svg>
</section>

<section class="features">
  <svg class="band" width="1200" height="282" viewBox="0 0 1200 282">
    <defs><linearGradient id="bandg" x1="0" y1="0" x2="1" y2="1"><stop offset="0" stop-color="#0a64bb"/><stop offset="1" stop-color="#054a8c"/></linearGradient></defs>
    <polygon points="0,0 1200,0 1200,200 600,282 0,200" fill="url(#bandg)"/>
  </svg>
  <div class="divider" style="left:465px"></div>
  <div class="divider" style="left:744px"></div>
  <div class="feature" style="left:188px">
    <svg width="70" height="50" viewBox="0 0 70 50"><path d="M5 22l15-12 12 6 8-4 25 12-10 12-14-10-10 8z" fill="none" stroke="#fff" stroke-width="3" stroke-linejoin="round"/></svg>
    <h3>OUR SERVICES</h3>
    <p>Curabitur metus ipsum luctus eu malesuada<br>ut tincidunt sed diam Donec quis</p>
    <span class="more">READ MORE</span>
  </div>
  <div class="feature" style="left:465px">
    <svg width="70" height="60" viewBox="0 0 70 60"><rect x="16" y="4" width="28" height="44" rx="2" fill="none" stroke="#fff" stroke-width="2.5"/><path d="M22 14h16M22 22h16M22 30h10" stroke="#fff" stroke-width="2"/><circle cx="52" cy="44" r="8" fill="none" stroke="#fff" stroke-width="2.5"/></svg>
    <h3 style="margin-top:8px">ABOUT US</h3>
    <p>Curabitur metus ipsum luctus eu malesuada<br>ut tincidunt sed diam Donec quis</p>
    <span class="more">READ MORE</span>
  </div>
  <div class="feature" style="left:744px">
    <svg width="80" height="50" viewBox="0 0 80 50"><ellipse cx="38" cy="26" rx="24" ry="17" fill="#fff"/><rect x="26" y="38" width="6" height="10" fill="#fff"/><rect x="44" y="38" width="6" height="10" fill="#fff"/><rect x="60" y="20" width="8" height="10" rx="2" fill="#fff"/><rect x="32" y="12" width="12" height="3" fill="#0758a4"/></svg>
    <h3>RESOURCES</h3>
    <p>Curabitur metus ipsum luctus eu malesuada<br>ut tincidunt sed diam Donec quis</p>
    <span class="more">READ MORE</span>
  </div>
</section>

<section class="block" style="top:883px;height:298px;background:#fff">
  <div style="position:absolute;left:186px;top:56px;width:388px">
    <h2>Our Promise</h2>
    <p>Taxes can be hard! Here at brindlecove, we know how to help! Our qualified experts and specialists know that your time is valuable.</p>
    <p style="margin-top:8px">That's why you're here—because you trust us to make the difference to put money back in your pocket. Dynamic, engaging and fast—that's why people choose brindlecove. We get the job done—not at someone else's pace and comfort level, but at yours!</p>
  </div>
  <div class="ph" role="img" aria-label="Smiling businessman writing a promise message on a glass board" style="left:596px;top:30px;width:446px;height:268px;background:linear-gradient(135deg,#f4f5f7,#dfe3e8 55%,#c7ccd3)"></div>
</section>

<section class="block" style="top:1181px;height:347px;background:linear-gradient(160deg,#f0f0f0,#e6e6e6);border-top:1px solid var(--line)">
  <div class="chev" style="top:-22px"><svg width="14" height="9" viewBox="0 0 14 9"><path d="M1 1l6 6 6-6" stroke="#333" stroke-width="2" fill="none"/></svg></div>
  <div class="ph" role="img" aria-label="Illustration of a clipboard story sheet, calculator, pencil and eraser" style="left:190px;top:46px;width:320px;height:260px;background:linear-gradient(135deg,#e4d8c8,#c9a880 60%,#b48c62);border-radius:4px"></div>
  <div style="position:absolute;left:584px;top:72px;width:420px">
    <h2>Our Story</h2>
    <p>Our team is small. Our experts come from a lot of places, but we all arrived here for a reason—because we're passionate about advocating for your wallet. Our services are valuable because we offer fast resolution that puts money back in your pocket. You deserve us.</p>
    <p style="margin-top:8px">We know we deserve you. Moving forward and making your taxes a stress-free process isn't hard—it's just us. It's brindlecove. It's why our clients keep coming back, year after year.</p>
  </div>
</section>

<section class="block" style="top:1528px;height:298px;background:#fff;border-top:1px solid var(--line)">
  <div style="position:absolute;left:178px;top:52px;width:490px">
    <h2>Save Money</h2>
    <p>Taxes can be hard! Here at brindlecove, we know how to help! Our qualified experts and specialists know that your time is valuable.</p>
    <p style="margin-top:8px">That's why you're here—because you trust us to make the difference to put money back in your pocket. Dynamic, engaging and fast—that's why people choose brindlecove. We get the job done—not at someone else's pace and comfort level, but at yours!</p>
  </div>
  <div class="ph" role="img" aria-label="Illustration of a hand dropping a gold coin into a piggy bank" style="left:760px;top:26px;width:216px;height:250px;background:linear-gradient(160deg,#f6c36a,#f28c5a 55%,#ee7b55);border-radius:6px"></div>
</section>

<section class="referral">
  <div class="shade" role="img" aria-label="Tax forms and a calculator on a desk"></div>
  <div class="chev" style="top:-22px"><svg width="14" height="9" viewBox="0 0 14 9"><path d="M1 1l6 6 6-6" stroke="#333" stroke-width="2" fill="none"/></svg></div>
  <h2>Take advantage of my Referral Rewards</h2>
  <h3>Program for even more savings.</h3>
  <p class="lead">Receive a rebate on service fees with this exciting promotion!</p>

  <div class="card" style="left:204px">
    <div class="top" style="background:#1677d2">
      <svg class="hex" width="100" height="116" viewBox="0 0 100 116"><polygon points="50,3 96,30 96,86 50,113 4,86 4,30" fill="none" stroke="#fff" stroke-width="2"/></svg>
      <div class="save"><small>SAVE</small><b>25%</b></div>
    </div>
    <div class="label" style="background:#0d63b5">1 REFERRALS</div>
  </div>
  <div class="card" style="left:474px">
    <div class="top" style="background:var(--blue)">
      <svg class="hex" width="100" height="116" viewBox="0 0 100 116"><polygon points="50,3 96,30 96,86 50,113 4,86 4,30" fill="none" stroke="#fff" stroke-width="2"/></svg>
      <div class="save"><small>SAVE</small><b>50%</b></div>
    </div>
    <div class="label" style="background:var(--blue-deep)">2 REFERRALS</div>
  </div>
  <div class="card" style="left:744px">
    <div class="top" style="background:var(--green)">
      <svg class="hex" width="100" height="116" viewBox="0 0 100 116"><polygon points="50,3 96,30 96,86 50,113 4,86 4,30" fill="none" stroke="#fff" stroke-width="2"/></svg>
      <div class="save"><small>SAVE</small><b>100%</b></div>
    </div>
    <div class="label" style="background:#55961a">3 REFERRALS</div>
  </div>
</section>

<section class="faq">
  <h2>Have any questions?</h2>
  <div class="acc">
    <div class="row open"><b>Q:</b>Are you able to accommodate my busy schedule?
      <span class="tog"><svg width="10" height="2"><rect width="10" height="2" fill="#0758a4"/></svg></span></div>
    <div class="answer"><b>A:</b>My flexible hours are designed to work around your demanding schedule, so I make myself available in the evenings and on weekends. In addition, you can choose how we work together—by phone, email, video call, or in person.</div>
    <div class="row"><b>Q:</b>How soon will you file my taxes after my initial consultation?
      <span class="tog"><svg width="10" height="10"><path d="M5 0v10M0 5h10" stroke="#fff" stroke-width="2"/></svg></span></div>
    <div class="row"><b>Q:</b>Are you available after the April 15th tax deadline?
      <span class="tog"><svg width="10" height="10"><path d="M5 0v10M0 5h10" stroke="#fff" stroke-width="2"/></svg></span></div>
    <div class="row"><b>Q:</b>How can I track my return?
      <span class="tog"><svg width="10" height="10"><path d="M5 0v10M0 5h10" stroke="#fff" stroke-width="2"/></svg></span></div>
  </div>
</section>

<section class="signup">
  <h2>Sign Up Today!</h2>
  <div class="field" style="left:250px;top:94px;width:228px">Name</div>
  <div class="field" style="left:489px;top:94px;width:228px">Email address</div>
  <div class="field" style="left:728px;top:94px;width:230px">Phone</div>
  <div class="field" style="left:250px;top:136px;width:228px">Subject</div>
  <div class="field" style="left:489px;top:136px;width:228px">Message</div>
  <div class="register">REGISTER</div>
</section>

<footer class="footer">
  <div class="fcol" style="left:187px"><h4>COMPANY</h4><ul><li>Home</li><li>About Us</li><li>Our Projects</li><li>Our Team</li></ul></div>
  <div class="fcol" style="left:319px"><h4>RESOURCES</h4><ul><li>Services</li><li>Our Partners</li><li>Career</li><li>Contact Us</li></ul></div>
  <div class="fcol" style="left:468px"><h4>NEWSLETTER SIGN UP</h4>
    <p style="font-size:10.5px;color:#ccc">Please Sign up here for latest news</p>
    <div class="news-in">Enter your email</div>
    <span class="sub-btn">SUBSCRIBE</span>
  </div>
  <div class="fcol contact" style="left:696px"><h4>CONTACT INFO</h4>
    <ul>
      <li>120 Harbor Lane Suite 4B</li>
      <li><svg width="10" height="10" viewBox="0 0 12 12"><path d="M3 1l2 2-1 1.5a7 7 0 003.5 3.5L9 7l2 2-1.5 2C5 11 1 7 1 2.5z" fill="#ccc"/></svg>(555) 212-0148</li>
      <li><svg width="11" height="8" viewBox="0 0 14 10"><rect width="14" height="10" rx="1" fill="#ccc"/><path d="M0 1l7 5 7-5" stroke="#1b1b1b" fill="none"/></svg>office@brindlecove.com</li>
    </ul>
    <div class="socials"><span></span><span></span><span></span><span></span></div>
  </div>
  <div class="foot-brand"><i></i>brindlecove.com</div>
</footer>

<div class="bottombar"><p>© 2016 Company Name. All right reserved. Term of Use</p></div>

</body>
</html>
```